Web-page design

We need a initial web design for our page kelbrook.com.au (which is not yet set up).
We provide consulting services for all kinds of problems in and between organisations.
Main focus is on conflict resolution but we also support companies on improving their operational performance.
We want to have the following page structure (and part of the project is to design the 8 pages):
- Home
- Services (we offer 3 main service areas - one per page)
- Case studies (one per page)
- Engaging us (our process)
- About Conflict & low performance
- Conflict resolution App
- About
- Contact (Email form)
- Our logo should be on each page.
The start page should include the following information:
- Twitter / Linkedin / facebook/ google + Links
- Telephone / Email or in general contact details
- News
- A quite prominent picture box with 3 alternating pics - each representing one of our service areas
- Link to our App
- Testimonials
It would be nice if the service pages would have an image header. Links to the information section (about conflict & low performance; and the app page) would be nice as well.
We like the following joomla designs: www.frandelthemes.com/itempreview/153
No need to copy it, it should just give you an idea.
We like the layout here with the picture and space for the case studies on the left. Somewhere beneath should be the 3 service areas with a picture each.
In terms of colors: our logo colours are Blue (RBG 8;44;80) and Orange (RGB 231;120;23). The orange could be used to emphasise certain things, however there should not be too much color.
Budget for images available, so please use placeholders or ask us for specific photos/images, if you need them for your design.
Updates
Hi, one more thing that we would like to have is the case studies not hidden behind a link "case studies" - we would like to have them individually linked prominent on the first page. There will be about 6-8 of them. Thats what we liked on the joomla template (the links left from the picture).
Hi, thanks very much for all the great proposals.
We are currently going through the selection process and will post our decision early next week.
Thanks again!
Wilma
Target Market(s)
- target customers are all different kinds of businesses and organisations (all industries, government, non-for-profit, ...) experiencing conflict and tension - be it with internal staff, amongst managers or board members, dysfunctional teams, between organizations or customers and organizations... examples could be bullying allegations, governmental negotiations with unions, disputes within organizations etc.
- also we will offer performance improvement services for organizations
- we will offer mediation, facilitation, negotiation, performance improvement services, conflict coaching, conflict management, change management services
- if comparable to anything - then to a law firm in terms of dealing with conflicts but its much less adversarial and much more about the people and their interests rather than about laws
- basically it's all kind of things you can do in order to solve disputes without involving lawyers and a court - so it's much cheaper and target is to find a solution all parties can live with rather than having a judge deciding about who wins and who looses
- performance management is more about analysing reasons for a lack of performance and setting up continous improvement systems, supporting change management, facilitating improvement workshops or strategic meetings, ...
Industry/Entity Type
Consulting
Look and feel

```html
<!DOCTYPE html>
<html lang="en">
<head>
<meta charset="utf-8">
<title>Kelbrook Resolve — Home</title>
<link href="https://fonts.googleapis.com/css2?family=Source+Sans+3:ital,wght@0,400;0,600;1,400&display=swap" rel="stylesheet">
<style>
:root{
  --navy:#0b2c50;
  --navy-light:#1d4a78;
  --orange:#e77817;
  --text:#3a3a3a;
  --muted:#8a8a8a;
  --rule:#d9d9d9;
  --panel:#f2f2f2;
  --footer:#333333;
}
*{box-sizing:border-box;margin:0;padding:0}
html,body{width:1071px;height:1200px;overflow:hidden;background:#fff}
body{position:relative;font-family:"Source Sans 3",Arial,sans-serif;color:var(--text)}
.abs{position:absolute}

.brand{left:91px;top:28px;display:flex;align-items:center;gap:10px}
.brand-mark{width:26px;height:26px;border:3px solid var(--orange)}
.brand-name{font-size:30px;color:var(--navy);letter-spacing:.5px}
.brand-url{left:117px;top:76px;font-size:12px;letter-spacing:8px;color:var(--navy)}

.contact-line{right:89px;font-size:16px;color:#555;display:flex;align-items:center;gap:10px}
.contact-line svg{width:18px;height:14px}

.main-nav{left:88px;top:110px;width:894px;height:45px;display:flex;border-radius:3px;overflow:hidden;
  background:linear-gradient(#2b5a8a,var(--navy))}
.main-nav a{height:45px;display:flex;align-items:center;justify-content:center;color:#fff;text-decoration:none;
  font-size:14.5px;border-right:1px solid #0a2440}
.main-nav a.current{background:linear-gradient(#f4a052,var(--orange));color:#222}

.hero{left:88px;top:162px;width:894px;height:328px;background:var(--panel);border:1px solid #ddd;border-radius:3px}
.hero-inner{position:absolute;left:10px;top:9px;width:873px;height:308px;background:#fafafa;overflow:hidden}
.hero-photo{position:absolute;right:0;top:0;width:470px;height:308px;
  background:linear-gradient(90deg,#fafafa 0%,#dfe8f0 25%,#9fc2e2 55%,#c7d6e4 80%,#eef1f4 100%)}
.hero-title{left:35px;top:34px;font-size:23px;font-weight:600;color:var(--orange)}
.hero-text{left:34px;top:74px;width:368px;font-size:13px;line-height:22.4px;text-align:justify}
.hero-btn{left:35px;top:199px;width:103px;height:34px;border:1px solid #8796a6;border-radius:2px;
  background:linear-gradient(#a9b6c3,#8393a5);color:#fff;font-size:17px;display:flex;align-items:center;justify-content:center}
.hero-dots{left:36px;top:277px;display:flex;gap:8px}
.hero-dots span{width:13px;height:13px;border-radius:50%;background:#b8b8b8;border:1px solid #999}
.hero-dots span.on{background:#666}

.service{width:278px}
.service h2{font-size:25px;font-weight:400;color:var(--navy)}
.service .frame{margin-top:8px;height:148px;background:var(--panel);border:1px solid #e3e3e3;padding:7px}
.service .pic{width:100%;height:133px}

.section-title{display:flex;align-items:center;gap:10px;font-size:25px;color:var(--navy)}
.news{left:99px;top:733px;width:277px}
.news-head{height:42px;border-bottom:3px solid #8b9bb0;position:relative}
.news-arrows{position:absolute;right:0;top:12px;display:flex;gap:14px}
.news-item{position:relative;padding-left:31px;margin-top:20px}
.news-item:first-of-type{margin-top:22px}
.news-item svg{position:absolute;left:5px;top:4px}
.item-title{font-size:14px;color:var(--orange)}
.item-text{font-size:13px;line-height:18.6px;color:#555;margin-top:3px}
.item-date{font-size:10.5px;color:var(--muted);margin-top:4px}

.app{left:416px;top:733px;width:557px}
.app-text{margin-top:18px;width:453px;font-size:13px;line-height:20.5px;color:#555;text-align:justify}
.badges{margin-top:16px;display:flex;gap:6px}
.badges span{width:110px;height:36px;background:#1b1b1b;border-radius:3px;border:1px solid #555}
.phone{left:895px;top:740px;width:72px;height:170px;border-radius:12px;
  background:linear-gradient(#f4f4f4,#d6d6d6);border:1px solid #ccc}
.divider{left:416px;top:919px;width:557px;height:1px;background:var(--rule)}
.testimonials{left:416px;top:938px;width:557px}
.quote{font-size:13px;font-style:italic;line-height:18.6px;color:#555;margin-top:6px;text-indent:14px}

.site-footer{left:0;top:1092px;width:1071px;height:108px;background:var(--footer)}
.footer-nav{position:absolute;left:0;width:100%;top:22px;text-align:center;font-size:13.5px;color:#ddd}
.footer-nav a{color:#ddd;text-decoration:none}
.footer-nav i{font-style:normal;margin:0 8px;color:#aaa}
.copyright{position:absolute;left:90px;top:64px;font-size:13px;color:#ccc;word-spacing:2px}
.social{position:absolute;left:848px;top:61px;display:flex;gap:14px}
.social span{width:23px;height:23px;background:#d5d5d5;border-radius:2px}
</style>
</head>
<body>

<header>
  <div class="abs brand"><span class="brand-mark"></span><span class="brand-name">KELBROOK PARTNERS</span></div>
  <div class="abs brand-url">www.kelbrook.com.au</div>
  <div class="abs contact-line" style="top:28px">Call us : 555 014 2290
    <svg viewBox="0 0 18 14"><path d="M3 2c2-1 3 0 3 2L5 6c1 2 3 4 5 5l2-1c2 0 3 1 2 3-3 2-12-6-11-11z" fill="#555"/></svg></div>
  <div class="abs contact-line" style="top:60px">E-mail : info@kelbrook.com.au
    <svg viewBox="0 0 18 14"><path d="M2 6l7-4 7 4v6H2z" fill="none" stroke="#555" stroke-width="1.5"/><path d="M2 6l7 4 7-4" fill="none" stroke="#555" stroke-width="1.5"/></svg></div>
</header>

<nav class="abs main-nav">
  <a class="current" href="#" style="width:71px">Home</a>
  <a href="#" style="width:78px">Services</a>
  <a href="#" style="width:102px">Case studies</a>
  <a href="#" style="width:103px">Engaging us</a>
  <a href="#" style="width:230px">About Conflict &amp; low performance</a>
  <a href="#" style="width:164px">Conflict resolution App</a>
  <a href="#" style="width:65px">About</a>
  <a href="#" style="width:81px;border-right:none">Contact</a>
</nav>

<section class="abs hero">
  <div class="hero-inner">
    <div class="hero-photo" role="img" aria-label="Photo of two businessmen in a consulting meeting"></div>
    <h1 class="abs hero-title">Welcome to Kelbrook Resolve</h1>
    <p class="abs hero-text">Nullam risus nisi, blandit a convallis nec, vehicula quis augue. Donec sed lobortis eros, at commodo magna. Fusce ullamcorper, purus ut imperdiet luctus, arcu felis accumsan nulla, ut mollis arcu lectus quis erat. Morbi enim turpis, sollicitudin vel elementum non, tempor ac velit. Phasellus quis orci ante.</p>
    <div class="abs hero-btn">Contact us</div>
    <div class="abs hero-dots"><span class="on"></span><span></span><span></span><span></span></div>
  </div>
</section>

<section class="abs service" style="left:99px;top:507px">
  <h2>Assess</h2>
  <div class="frame"><div class="pic" role="img" aria-label="Photo of a business team around a meeting table" style="background:linear-gradient(90deg,#d9dde6,#a8aac8 50%,#e0e3ea)"></div></div>
</section>
<section class="abs service" style="left:397px;top:507px">
  <h2>Resolve</h2>
  <div class="frame"><div class="pic" role="img" aria-label="Image of a hand placing the last puzzle piece on blue" style="background:linear-gradient(135deg,#0e3a78,#2a74b8 60%,#1a5aa0)"></div></div>
</section>
<section class="abs service" style="left:696px;top:507px">
  <h2>Develop</h2>
  <div class="frame"><div class="pic" role="img" aria-label="Image of hands holding a rising growth arrow" style="background:linear-gradient(#1a1a1a,#3a3a3a 60%,#111)"></div></div>
</section>

<section class="abs news">
  <div class="news-head">
    <div class="section-title">
      <svg width="22" height="18" viewBox="0 0 22 18"><rect x="1" y="1" width="20" height="16" fill="none" stroke="#0b2c50" stroke-width="2"/><rect x="4" y="5" width="6" height="6" fill="#0b2c50"/><path d="M12 5h6M12 8h6M12 11h6M4 14h14" stroke="#0b2c50" stroke-width="1.5"/></svg>
      Latest News</div>
    <div class="news-arrows">
      <svg width="8" height="12"><path d="M7 1L2 6l5 5" fill="none" stroke="#888" stroke-width="2"/></svg>
      <svg width="8" height="12"><path d="M1 1l5 5-5 5" fill="none" stroke="#888" stroke-width="2"/></svg>
    </div>
  </div>
  <article class="news-item">
    <svg width="12" height="12"><path d="M2 1l5 5-5 5" fill="none" stroke="#999" stroke-width="1.3"/><path d="M11 0v12" stroke="#ccc"/></svg>
    <div class="item-title">Pellentesque bibendum</div>
    <p class="item-text">Cras bibendum dolor eget elit vehicula, non euismod dolor feugiat.</p>
    <div class="item-date">September - 16 - 2013</div>
  </article>
  <article class="news-item">
    <svg width="12" height="12"><path d="M2 1l5 5-5 5" fill="none" stroke="#999" stroke-width="1.3"/><path d="M11 0v12" stroke="#ccc"/></svg>
    <div class="item-title">Pellentesque bibendum</div>
    <p class="item-text">Cras bibendum dolor eget elit vehicula, non euismod dolor feugiat.</p>
    <div class="item-date">September - 16 - 2013</div>
  </article>
  <article class="news-item">
    <svg width="12" height="12"><path d="M2 1l5 5-5 5" fill="none" stroke="#999" stroke-width="1.3"/><path d="M11 0v12" stroke="#ccc"/></svg>
    <div class="item-title">Pellentesque bibendum</div>
    <p class="item-text">Cras bibendum dolor eget elit vehicula, non euismod dolor feugiat.</p>
    <div class="item-date">September - 16 - 2013</div>
  </article>
</section>

<section class="abs app">
  <div class="section-title">
    <svg width="11" height="17" viewBox="0 0 11 17"><rect x="1" y="1" width="9" height="15" rx="1" fill="none" stroke="#0b2c50" stroke-width="2"/><rect x="3" y="3" width="5" height="9" fill="#0b2c50"/></svg>
    Conflict resolution App</div>
  <p class="app-text">Aliquam vestibulum erat nec quam interdum, condimentum tincidunt lacus lobortis. Curabitur id ligula aliquam, egestas tellus non, fringilla velit. Donec pellentesque augue non felis laoreet posuere. In eget dignissim quam.</p>
  <div class="badges"><span></span><span style="width:107px"></span></div>
</section>
<div class="abs phone" role="img" aria-label="Image of a smartphone showing the app"></div>
<div class="abs divider"></div>

<section class="abs testimonials">
  <div class="section-title" style="justify-content:space-between">
    <span style="display:flex;align-items:center;gap:8px">
      <svg width="22" height="20" viewBox="0 0 22 20"><ellipse cx="11" cy="9" rx="10.5" ry="8.5" fill="#0b2c50"/><path d="M3 14l-2 5 7-3z" fill="#0b2c50"/></svg>
      Testimonials</span>
    <svg width="8" height="12" style="margin-right:4px"><path d="M1 1l5 5-5 5" fill="none" stroke="#888" stroke-width="2"/></svg>
  </div>
  <div class="item-title" style="margin-top:12px">Pellentesque bibendum</div>
  <p class="quote">“Suspendisse porta quam dolor pellentesque dapibus. Aenean eget bibendum magna. Etiam vestibulum fermentum magna vitae vestibulum.”</p>
  <div class="item-date">September - 16 - 2013</div>
</section>

<footer class="abs site-footer">
  <nav class="footer-nav">
    <a href="#">Home</a><i>|</i><a href="#">Services</a><i>|</i><a href="#">Case studies</a><i>|</i><a href="#">Engaging us</a><i>|</i><a href="#">About Conflict &amp; low performance</a><i>|</i><a href="#">Conflict resolution App</a><i>|</i><a href="#">About</a><i>|</i><a href="#">Contact</a>
  </nav>
  <p class="copyright">Copyright © 2013 Kelbrook Resolve. All rights reserved.</p>
  <div class="social"><span></span><span></span><span></span><span></span></div>
</footer>

</body>
</html>
```